New Church Plant website for Brightvale Church

I would like a six page website designed that is clean and easy to navigate. The six pages will include (1) About Us (2) Home (3) Contact Us (4) Sermons (5) Donate (6) Ministries. There will be subcategories for each category as well. The color scheme can be found in the attached magazine of Brightvale. Much of the information found in the booklet will be used on the website. I would love to see a design that pops but still clean and easy to navigate. I have included a good deal of pictures for the creative. Please see the current website at brightvalechurch.example which is temporary as we are preparing for a launch. I would now like to create a long-term site.

Target Market(s)

People interested in Christian church

Number of Pages Required

5+ page

Font styles to use
Sans Serif

Colors
ffffff
f78f20

Requirements
Must have
• a site that pops but is clean and easy to navigate.

```html
<!DOCTYPE html>
<html lang="en">
<head>
<meta charset="utf-8">
<title>Brightvale Church — Home</title>
<link rel="stylesheet" href="https://fonts.googleapis.com/css2?family=Montserrat:wght@400;500;600;700&family=Lato:wght@400;700&display=swap">
<style>
:root{
  --orange:#f78f20;
  --orange-deep:#f06a12;
  --white:#ffffff;
  --ink:#2b2b2b;
  --text:#4a4a4a;
  --night:#0d0d0f;
  --brown:#3a2117;
  --grey:#e9e9e9;
}
*{margin:0;padding:0;box-sizing:border-box}
html,body{width:1200px;height:3474px;overflow:hidden;background:var(--white)}
body{position:relative;font-family:"Lato",sans-serif;color:var(--text)}
.abs{position:absolute}
.heading{font-family:"Montserrat",sans-serif;font-weight:700;text-transform:uppercase;color:var(--ink)}
.btn{position:absolute;display:flex;align-items:center;justify-content:center;border-radius:30px;font-family:"Montserrat",sans-serif;font-weight:500;font-size:16px;text-transform:uppercase;text-decoration:none}
.btn-solid{background:var(--orange);color:var(--white)}
.btn-outline{border:2px solid var(--orange);color:var(--orange)}
.btn-white{background:var(--white);color:var(--orange)}

/* header */
.site-header{left:0;top:0;width:1200px;height:92px;background:var(--white);z-index:5}
.brand{left:162px;top:26px;font-family:"Montserrat",sans-serif;font-weight:600;font-size:30px;color:var(--orange);display:flex;align-items:center;gap:10px}
.brand-dot{width:14px;height:14px;border-radius:50%;background:var(--orange)}
.main-nav{left:434px;top:43px;display:flex;font-family:"Montserrat",sans-serif;font-weight:600;font-size:14px;color:var(--ink)}
.main-nav span{padding:0 20px;border-left:1px solid #777;line-height:14px}
.main-nav span:first-child{border:none;padding-left:0;color:var(--orange)}

/* hero */
.hero{left:0;top:92px;width:1200px;height:710px;background:linear-gradient(90deg,#070809 0%,#141821 45%,#2a1c14 70%,#4a2a12 100%)}
.hero-stage{left:0;top:520px;width:1200px;height:190px;background:linear-gradient(180deg,#5a3512,#8a4e17 60%,#2a1808)}
.hero-photo{left:740px;top:50px;width:320px;height:680px;background:radial-gradient(ellipse at 50% 40%,#8a4a34 0%,#4a2d26 45%,rgba(20,20,30,0) 75%)}
.hero-title{left:158px;top:278px;font-family:"Montserrat",sans-serif;font-size:46px;line-height:50px;color:var(--white);text-transform:uppercase}
.hero-title b{color:var(--orange);font-weight:700}
.hero-title span{font-weight:400}
.hero-text{left:162px;top:386px;width:490px;font-family:"Montserrat",sans-serif;font-size:16px;line-height:25px;color:var(--white)}
.hero-dots{left:557px;top:692px;display:flex;gap:8px}
.hero-dots i{width:14px;height:14px;border-radius:50%;background:var(--white);display:block}
.hero-dots i:first-child{background:transparent;border:2px solid var(--white)}

/* about */
.about-mark{left:160px;top:930px;width:420px;font-family:"Montserrat",sans-serif;font-weight:700;font-size:64px;line-height:80px;color:var(--orange)}
.about-title{left:611px;top:880px;font-size:29px}
.about-copy{left:611px;top:938px;width:470px;font-size:16px;line-height:22px}
.about-copy p{margin-bottom:11px}

/* community */
.community{left:0;top:1222px;width:1200px;height:660px;background:linear-gradient(90deg,#2b1710 0%,#4b2a1c 45%,#6b3a22 70%,#3a2117 100%)}
.community-photo{left:640px;top:50px;width:560px;height:610px;background:radial-gradient(ellipse at 35% 45%,#c9502a 0%,#8a3a1f 35%,rgba(40,22,15,0) 70%),radial-gradient(ellipse at 80% 55%,#2a2222 0%,rgba(0,0,0,0) 60%)}
.community-title{left:151px;top:1390px;font-size:29px;color:var(--white)}
.checklist{left:150px;top:1454px;width:440px;list-style:none;color:var(--white);font-size:15.5px;line-height:22px}
.checklist li{display:flex;gap:9px;margin-bottom:22px}
.checklist svg{flex:none;margin-top:3px}

/* panels */
.mission{left:0;top:1813px;width:607px;height:520px;background:linear-gradient(90deg,#f2f2f2,#dcdcdc 60%,#bdbdbd)}
.donate-panel{left:607px;top:1813px;width:593px;height:520px;background:linear-gradient(180deg,#f36e14,#f38a2a 60%,#f07a1a)}
.panel-title{width:600px;text-align:center;font-size:25px}
.panel-copy{width:420px;text-align:center;font-size:15px;line-height:21px}

/* testimonial */
.speaker-photo{left:183px;top:2427px;width:260px;height:260px;border-radius:50%;background:radial-gradient(circle at 50% 55%,#6a3a22 0%,#8fbf4a 45%,#e8f0d0 100%)}
.quote-mark{font-family:"Montserrat",sans-serif;font-weight:700;font-size:90px;line-height:90px;color:var(--orange)}
.quote-text{left:524px;top:2472px;width:470px;font-family:"Montserrat",sans-serif;font-weight:600;font-size:23px;line-height:32px;color:var(--ink);text-transform:uppercase;white-space:nowrap}
.quote-name{left:524px;top:2618px;font-family:"Montserrat",sans-serif;font-weight:700;font-size:16px;color:var(--orange)}

/* launch */
.launch{left:0;top:2736px;width:1200px;height:520px;background:linear-gradient(160deg,#101010 0%,#3a3a3a 45%,#5a5a5a 60%,#1a1a1a 100%)}
.launch-title{left:0;top:2915px;width:1200px;text-align:center;font-size:39px;color:var(--white)}
.launch-title span{color:var(--orange)}
.launch-sub{left:0;top:2972px;width:1200px;text-align:center;font-family:"Montserrat",sans-serif;font-weight:700;font-size:19px;line-height:30px;color:var(--white)}

/* footer */
.site-footer{left:0;top:3230px;width:1200px;height:244px;background:var(--night)}
.footer-brand{left:0;top:3245px;width:1200px;display:flex;justify-content:center;font-family:"Montserrat",sans-serif;font-weight:600;font-size:30px;color:var(--white)}
.footer-nav{left:0;top:3324px;width:1200px;display:flex;justify-content:center;gap:46px;font-family:"Montserrat",sans-serif;font-weight:600;font-size:14px;color:var(--white)}
.copyright{left:0;top:3350px;width:1200px;text-align:center;font-family:"Montserrat",sans-serif;font-size:12px;color:#bbb}
.social{left:527px;top:3383px;display:flex;gap:9px}
.social i{display:block;width:46px;height:46px;border-radius:50%;background:var(--orange)}
</style>
</head>
<body>

<header class="abs site-header">
  <div class="abs brand"><span class="brand-dot"></span>Brightvale</div>
  <nav class="abs main-nav">
    <span>HOME</span><span>ABOUT US</span><span>CONTACT US</span><span>SERMONS</span><span>DONATE</span><span>MINISTRIES</span>
  </nav>
</header>

<section class="abs hero">
  <div class="abs hero-stage" role="img" aria-label="Church stage floor with stool and music stand"></div>
  <div class="abs hero-photo" role="img" aria-label="Pastor speaking on stage in an argyle sweater"></div>
</section>
<h1 class="abs hero-title"><b>Multi-Ethnic</b><br><span>Church Planting</span></h1>
<p class="abs hero-text">A Riverton-based, multi-ethnic, gospel-centered, church<br>planting church built on the pillars of missions</p>
<a class="btn btn-solid" style="left:162px;top:458px;width:178px;height:56px;font-size:18px">Donate</a>
<div class="abs hero-dots"><i></i><i></i><i></i><i></i></div>

<svg class="abs" style="left:0;top:730px" width="1200" height="80" viewBox="0 0 1200 80">
  <path d="M0 72 Q600 -60 1200 72 L1200 80 L0 80Z" fill="#fff"/>
</svg>

<div class="abs about-mark">Brightvale</div>
<h2 class="abs heading about-title">Brightvale Church</h2>
<div class="abs about-copy">
  <p>Vivamus porttitor neque at volutpat rutrum purus nisi eleifend libero a tempus libero lectus feugiat felis Morbi diam mauris viverra in gravida eu mattis in ante Morbi eget arcu</p>
  <p>Morbi porta libero id ullamcorper nonummy nibh ligula pulvinar metus eget consectetuer augue nisi quis Curabitur vel mi sit amet magna malesuada ultrices Ut nisi erat fermentum ve</p>
</div>
<a class="btn btn-outline" style="left:607px;top:1108px;width:163px;height:50px">Learn More</a>

<section class="abs community">
  <div class="abs community-photo" role="img" aria-label="Smiling couple, husband in orange sweater and wife in black top"></div>
</section>
<svg class="abs" style="left:0;top:1220px" width="1200" height="60" viewBox="0 0 1200 60">
  <path d="M0 0 L1200 0 L1200 4 Q600 70 0 4Z" fill="#fff"/>
  <path d="M170 22 Q600 60 1020 22" stroke="#f78f20" stroke-width="4" fill="none"/>
</svg>
<h2 class="abs heading community-title">Community Connection</h2>
<ul class="abs checklist">
  <li><svg width="16" height="16" viewBox="0 0 16 16"><circle cx="8" cy="8" r="7" fill="none" stroke="#fff" stroke-width="1.4"/><path d="M4.5 8l2.5 2.5L13 4" fill="none" stroke="#fff" stroke-width="1.6"/></svg>Vivamus porttitor neque at volutpat rutrum purus nisi eleifend libero a tempus libero lectus feugiat felis</li>
  <li><svg width="16" height="16" viewBox="0 0 16 16"><circle cx="8" cy="8" r="7" fill="none" stroke="#fff" stroke-width="1.4"/><path d="M4.5 8l2.5 2.5L13 4" fill="none" stroke="#fff" stroke-width="1.6"/></svg>Morbi diam mauris viverra in gravida eu mattis in ante Morbi eget arcu Morbi porta libero id ullamcorper</li>
  <li><svg width="16" height="16" viewBox="0 0 16 16"><circle cx="8" cy="8" r="7" fill="none" stroke="#fff" stroke-width="1.4"/><path d="M4.5 8l2.5 2.5L13 4" fill="none" stroke="#fff" stroke-width="1.6"/></svg>Aonummy nibh ligula pulvinar metus eget consectetuer</li>
  <li><svg width="16" height="16" viewBox="0 0 16 16"><circle cx="8" cy="8" r="7" fill="none" stroke="#fff" stroke-width="1.4"/><path d="M4.5 8l2.5 2.5L13 4" fill="none" stroke="#fff" stroke-width="1.6"/></svg>Curabitur vel mi sit amet magna malesuada ultrices Ut nisi erat fermentum vel congue id euismod in elit</li>
</ul>
<a class="btn btn-outline" style="left:148px;top:1703px;width:163px;height:50px">Learn More</a>

<section class="abs mission" role="img" aria-label="Greyscale photo of a man seated at a table"></section>
<section class="abs donate-panel" role="img" aria-label="Orange-toned photo of a smiling woman"></section>
<svg class="abs" style="left:0;top:1810px" width="1200" height="70" viewBox="0 0 1200 70">
  <path d="M0 0 L607 0 L607 3 Q300 20 0 70Z" fill="#3a2117"/>
  <path d="M607 3 L1200 3 L1200 60 Q900 0 607 3Z" fill="#3a2117"/>
</svg>

<svg class="abs" style="left:285px;top:1919px" width="104" height="104" viewBox="0 0 104 104">
  <circle cx="52" cy="52" r="50" fill="none" stroke="#444" stroke-width="2"/>
  <circle cx="52" cy="52" r="24" fill="none" stroke="#444" stroke-width="2"/>
  <circle cx="52" cy="52" r="16" fill="none" stroke="#444" stroke-width="2"/>
  <circle cx="52" cy="52" r="8" fill="none" stroke="#444" stroke-width="2"/>
  <path d="M52 52 L72 32 M68 30 h6 v6" stroke="#444" stroke-width="2" fill="none"/>
</svg>
<h2 class="abs heading panel-title" style="left:34px;top:2040px">Our Mission</h2>
<p class="abs panel-copy" style="left:124px;top:2082px;color:#555">To be gospel centered, multi-ethnic, church planting church built on the pillars of missions, faith, work and economicsMorbi diam mauris viverra in gravida eu mattis in ante Morbi eget arcu Morbi porta libero id ullamcorper nonu</p>
<a class="btn btn-solid" style="left:249px;top:2208px;width:160px;height:46px">Learn More</a>

<svg class="abs" style="left:835px;top:1920px" width="104" height="104" viewBox="0 0 104 104">
  <circle cx="52" cy="52" r="50" fill="none" stroke="#fff" stroke-width="2.5"/>
  <path d="M52 46 C44 38 36 44 42 52 L52 60 L62 52 C68 44 60 38 52 46Z" fill="none" stroke="#fff" stroke-width="2.5"/>
  <path d="M28 66 h10 l10 4 h12 a3 3 0 0 1 0 6 h-10 M38 78 h18 l16-8 a3 3 0 0 1 4 4 l-18 10 h-20 M26 62 v24 h10 v-24Z" fill="none" stroke="#fff" stroke-width="2.5"/>
</svg>
<h2 class="abs heading panel-title" style="left:584px;top:2040px;color:#fff">Donate</h2>
<p class="abs panel-copy" style="left:674px;top:2082px;color:#fff">Vivamus porttitor neque at volutpat rutrum purus nisi eleifend libero a tempus libero lectus feugiat felis Morbi diam mauris viverra in gravida eu mattis in ante Morbi eget arcu Morbi porta libero id ullamcorper nonu</p>
<a class="btn btn-white" style="left:807px;top:2208px;width:161px;height:46px">Donate Now</a>

<div class="abs speaker-photo" role="img" aria-label="Speaker in a brown jacket standing in front of a worship screen"></div>
<div class="abs quote-mark" style="left:460px;top:2466px">&ldquo;</div>
<blockquote class="abs quote-text">I value multi-ethnic ministry be-<br>cause I am the product of what<br>can happen through multi-<br>ethnic relationships</blockquote>
<div class="abs quote-mark" style="left:818px;top:2578px">&rdquo;</div>
<div class="abs quote-name">DANIEL REYES</div>

<section class="abs launch" role="img" aria-label="Close-up of hands playing an acoustic guitar"></section>
<svg class="abs" style="left:0;top:2734px" width="1200" height="72" viewBox="0 0 1200 72">
  <path d="M0 0 L1200 0 L1200 2 Q600 140 0 2Z" fill="#fff"/>
</svg>
<h2 class="abs heading launch-title">Launching <span>April 12, 2020</span></h2>
<p class="abs launch-sub">OAKRIDGE PREP (FORMERLY HALSTON)<br>AT 48TH AND OAKRIDGE RD</p>

<footer class="abs site-footer"></footer>
<svg class="abs" style="left:0;top:3195px" width="1200" height="60" viewBox="0 0 1200 60">
  <path d="M0 60 Q600 -30 1200 60Z" fill="#0d0d0f"/>
  <path d="M110 55 Q600 -20 1090 55" stroke="#f78f20" stroke-width="3" fill="none"/>
</svg>
<div class="abs footer-brand">Brightvale</div>
<nav class="abs footer-nav"><span>HOME</span><span>ABOUT US</span><span>CONTACT US</span><span>SERMONS</span><span>DONATE</span><span>MINISTRIES</span></nav>
<p class="abs copyright">© 2020 Company Name | All Rights Reserved | Disclaimer</p>
<div class="abs social" aria-label="Social links"><i></i><i></i><i></i></div>

</body>
</html>
```